Brindle Capital and Investments

Create a simple business card design using the logos attached. Make it similar but not exact to the reference photo. Brand guidelines are also included.

```html
<!DOCTYPE html>
<html lang="en">
<head>
<meta charset="utf-8">
<title>Brindle Capital — Business Card</title>
<link href="https://fonts.googleapis.com/css2?family=Crimson+Text:wght@400;600&family=PT+Sans+Narrow&display=swap" rel="stylesheet">
<style>
  :root {
    --backdrop: #c9c7c3;
    --card: #ffffff;
    --navy: #15213f;
    --ink: #1b1b1f;
    --copper: #b5651d;
  }
  html, body {
    margin: 0;
    width: 1200px;
    height: 1200px;
    overflow: hidden;
    background: var(--backdrop);
  }
  .card {
    position: absolute;
    left: 170px;
    top: 360px;
    width: 860px;
    height: 490px;
    background: var(--card);
    box-shadow: 0 6px 24px rgba(0,0,0,0.12);
    font-family: "Crimson Text", Georgia, serif;
  }
  .brand {
    position: absolute;
    left: 0;
    top: 0;
    width: 360px;
    height: 100%;
    display: flex;
    align-items: center;
    justify-content: center;
    gap: 14px;
  }
  .brand-dot {
    width: 16px;
    height: 16px;
    border-radius: 50%;
    background: var(--navy);
  }
  .brand-name {
    font-size: 38px;
    font-weight: 600;
    color: var(--navy);
    letter-spacing: 0.5px;
  }
  .divider {
    position: absolute;
    left: 360px;
    top: 70px;
    width: 2px;
    height: 350px;
    background: var(--copper);
  }
  .details {
    position: absolute;
    left: 430px;
    top: 78px;
    width: 380px;
  }
  .person-name {
    margin: 0;
    font-size: 38px;
    font-weight: 600;
    color: var(--navy);
    line-height: 1;
  }
  .person-title {
    margin: 6px 0 0;
    font-size: 25px;
    color: var(--copper);
    line-height: 1.1;
  }
  .email {
    margin: 36px 0 0;
    font-size: 28px;
    color: var(--ink);
    line-height: 1.1;
  }
  .phone {
    margin: 6px 0 0;
    font-family: "PT Sans Narrow", "Arial Narrow", sans-serif;
    font-size: 22px;
    color: var(--ink);
  }
  .rule {
    margin: 32px 0 0;
    width: 340px;
    height: 2px;
    background: var(--navy);
    border: 0;
  }
  .company {
    margin: 26px 0 0;
    font-size: 28px;
    color: var(--ink);
    line-height: 1.1;
  }
</style>
</head>
<body>
  <div class="card">
    <div class="brand">
      <span class="brand-dot"></span>
      <span class="brand-name">Brindle Capital</span>
    </div>
    <div class="divider"></div>
    <div class="details">
      <p class="person-name">Daniel Hayes</p>
      <p class="person-title">Managing Partner</p>
      <p class="email">dan@brindlecapital.com</p>
      <p class="phone">555.014.2287</p>
      <hr class="rule">
      <p class="company">Brindle Capital &amp; Investments<br>Fort Worth, Texas<br>brindlecapital.com</p>
    </div>
  </div>
</body>
</html>
```